Harborline Talent IT Recruiting firm needs a business card design for Recruiters, Sourcers, and Account

We need business cards that allow us to change all contact info, names, titles (Recruiter, Sourcer, Account Manager, Director, CEO, etc) per person since we have three offices, in three cities, Phoenix, Austin, and Las Vegas. We do recruiting and contractors for IT positions (Developers, Architects, Software Engineers, Security Engineers, Help Desk, DBAs, PMs, Scrum Masters, etc.) Our client companies are very diverse from Crestline 250 to silicone Valley type start-ups.

So, while we what hip, techie, and quirky, it still needs to be professional. Primary color we use is blue, with silver as a secondary color.

Target Market(s)

IT, Technology

Industry/Entity Type

Business

Contact Information for Business Card

Company name: Harborline Talent, Inc.
Website: www.harborlinetalent-example.com
Logos for ProCircle, Quillo, and Roomwall

Name, Title, Office Number, Cell Number, email

Font styles to use
Serif
Sans Serif

Colors
0455a3
d5d5d5

Requirements
Nice to have
• The grey I selected below is not necessary - but, would like silver included. I included a card design (File 3: HTI early trial example.jpg) that I had started on. It's very rough, and not quite what we're looking for, but what we did like is the logo, big, maybe a bit faded, off center, goes out of frame, etc. Still looking for other ideas - you are the pros! But, just an idea of a design element we liked.

```html
<!DOCTYPE html>
<html lang="en">
<head>
<meta charset="utf-8">
<title>Harborline Talent – Business Card</title>
<link rel="stylesheet" href="https://fonts.googleapis.com/css2?family=Cinzel:wght@400&family=Open+Sans:wght@300;400;600;700&display=swap">
<style>
  :root {
    --brand-blue: #0455a3;
    --silver: #d5d5d5;
    --ink: #3a3a3a;
    --ink-soft: #6b6b6b;
    --paper: #ffffff;
    --backdrop: #e8e8e6;
    --arc-edge: #2b2b2b;
  }
  * { box-sizing: border-box; margin: 0; padding: 0; }
  html, body {
    width: 1200px; height: 948px; overflow: hidden;
    background: var(--backdrop);
    font-family: "Open Sans", Arial, sans-serif;
  }
  .stage {
    position: relative; width: 1200px; height: 948px;
    display: flex; flex-direction: column; align-items: center; justify-content: center;
    gap: 48px;
  }
  .card {
    position: relative; width: 700px; height: 400px;
    background: var(--paper);
    box-shadow: 0 6px 18px rgba(0,0,0,.18);
    overflow: hidden;
  }
  .wordmark { display: flex; align-items: center; gap: 14px; }
  .wordmark-mark {
    width: 46px; height: 46px; border-radius: 50%;
    background: var(--brand-blue); flex: none;
  }
  .wordmark-name {
    font-weight: 300; color: var(--ink);
    font-size: 40px; line-height: 1.02; letter-spacing: 4px;
    text-transform: uppercase;
  }
  .tagline {
    font-family: "Cinzel", Georgia, serif;
    color: var(--ink-soft); font-size: 14px; letter-spacing: 3px;
    text-transform: uppercase;
  }

  /* Front */
  .card-front .brand { position: absolute; left: 70px; top: 50px; }
  .card-front .tagline { margin-top: 14px; margin-left: 60px; }
  .card-front .swoosh { position: absolute; inset: 0; }
  .contact {
    position: absolute; left: 392px; top: 218px;
    color: #fff; list-style: none;
  }
  .contact-name { font-weight: 700; font-size: 19px; }
  .contact-title { font-size: 13px; font-weight: 400; margin-bottom: 8px; }
  .contact-line {
    display: flex; align-items: center; gap: 8px;
    font-size: 12.5px; line-height: 21px; font-weight: 400;
  }
  .contact-icon { width: 13px; height: 13px; flex: none; }
  .social-dot {
    width: 13px; height: 13px; border-radius: 50%;
    background: #fff; flex: none;
  }

  /* Back */
  .card-back {
    display: flex; flex-direction: column; align-items: center; justify-content: center;
  }
  .card-back .tagline { margin-top: 16px; }
  .website {
    margin-top: 28px; font-weight: 700; font-size: 17px;
    color: var(--ink); letter-spacing: .5px;
  }
</style>
</head>
<body>
<main class="stage">

  <section class="card card-front" aria-label="Business card front">
    <svg class="swoosh" viewBox="0 0 700 400" width="700" height="400" aria-hidden="true">
      <path d="M216,400 C240,250 390,168 700,160 L700,400 Z" fill="var(--arc-edge)"/>
      <path d="M228,400 C252,258 398,176 700,170 L700,400 Z" fill="var(--brand-blue)"/>
    </svg>

    <div class="brand">
      <div class="wordmark">
        <span class="wordmark-mark"></span>
        <span class="wordmark-name">Harborline<br>Talent</span>
      </div>
      <p class="tagline">Connecting Tech Talent</p>
    </div>

    <ul class="contact">
      <li class="contact-name">Maren Holloway</li>
      <li class="contact-title">First Touch Ambassador</li>
      <li class="contact-line">
        <svg class="contact-icon" viewBox="0 0 16 16" aria-hidden="true"><circle cx="8" cy="8" r="7.5" fill="none" stroke="#fff"/><path d="M5.2 4.2l1.4 0 .6 1.8-.9.7c.5 1 1.2 1.8 2.2 2.3l.7-.9 1.8.6v1.4c0 .4-.4.8-.9.7-3-.4-5.3-2.7-5.7-5.7 0-.5.3-.9.8-.9z" fill="#fff"/></svg>
        555-010-4827
      </li>
      <li class="contact-line">
        <svg class="contact-icon" viewBox="0 0 16 16" aria-hidden="true"><circle cx="8" cy="8" r="8" fill="#fff"/><rect x="4" y="5" width="8" height="6" fill="none" stroke="var(--brand-blue)"/><path d="M4 5l4 3.2L12 5" fill="none" stroke="var(--brand-blue)"/></svg>
        maren@harborlinetalent-example.com
      </li>
      <li class="contact-line">
        <svg class="contact-icon" viewBox="0 0 16 16" aria-hidden="true"><circle cx="8" cy="8" r="7" fill="none" stroke="#fff"/><ellipse cx="8" cy="8" rx="3" ry="7" fill="none" stroke="#fff"/><path d="M1 8h14" stroke="#fff"/></svg>
        www.harborlinetalent-example.com
      </li>
      <li class="contact-line"><span class="social-dot"></span>@MarenHollowayHT</li>
      <li class="contact-line"><span class="social-dot"></span>@MarenHollowayHT</li>
    </ul>
  </section>

  <section class="card card-back" aria-label="Business card back">
    <div class="wordmark">
      <span class="wordmark-mark"></span>
      <span class="wordmark-name">Harborline<br>Talent</span>
    </div>
    <p class="tagline">Connecting Tech Talent</p>
    <p class="website">www.harborlinetalent-example.com</p>
  </section>

</main>
</body>
</html>
```